Profesional personal website needs design and business card

I need a business card with my professional name as a logo "Marlo Vitality" for my business. I am a Wellness Coach, consultant and trainer. So it should be professional, wellness oriented and modern.

Target Market(s)

Private clients, governments, corporations. Luxury and high market.

Industry/Entity Type

Health And Wellness

Contact Information for Business Card

Marlo Vitality should be the logo

Colors

Designer to choose colors to be used in the design.

Requirements
Must have
• Marlo Vitality
• Name: Tomás Arribal
• Wellness Coach, Consultant & Trainer.
• Website: www.marlovitality.example
• Phone:
• Spain (+34) 612 480 397
• (USA) +1 (555) 318 2046
Nice to have
• The most important is the design of "Marlo Vitality", as this is going to be my personal brand logo. It should be professional, wellness, high end and actual.
Should not have
• no golds, no baroque style..

```html
<!DOCTYPE html>
<html lang="en">
<head>
<meta charset="utf-8">
<title>Marlo Vitality – Business Card</title>
<link href="https://fonts.googleapis.com/css2?family=Montserrat:wght@600;700&family=Open+Sans:wght@400;600;700&display=swap" rel="stylesheet">
<style>
  :root {
    --stage: #4f95fe;
    --navy: #0f2f7a;
    --green: #8dc63f;
    --white: #ffffff;
    --ink: #111111;
  }
  * { margin: 0; padding: 0; box-sizing: border-box; }
  html, body { width: 1200px; height: 1200px; overflow: hidden; }
  body { background: var(--stage); position: relative; font-family: "Open Sans", sans-serif; }

  .card { position: absolute; left: 183px; width: 835px; background: var(--white); overflow: hidden; }
  .card--front { top: 103px; height: 488px; }
  .card--back { top: 615px; height: 480px; }

  .brand { position: absolute; display: flex; align-items: center; }
  .brand__dot { border-radius: 50%; background: var(--green); flex: none; }
  .brand__name { font-family: "Open Sans", sans-serif; font-weight: 700; color: var(--navy); white-space: nowrap; letter-spacing: 0.5px; }

  .card--front .brand { left: 95px; top: 215px; }
  .card--front .brand__dot { width: 70px; height: 70px; margin-right: 30px; }
  .card--front .brand__name { font-size: 58px; }

  .footer-band { position: absolute; left: 0; right: 0; bottom: 0; background: var(--navy); }
  .card--front .footer-band { height: 119px; }
  .footer-url { position: absolute; left: 55px; color: var(--white); font-weight: 600; font-size: 22px; letter-spacing: 0.2px; }
  .card--front .footer-url { top: 44px; }
  .social { position: absolute; right: 45px; display: flex; gap: 15px; }
  .card--front .social { top: 35px; }
  .social__item { width: 50px; height: 50px; border-radius: 50%; background: var(--white); }

  .person { position: absolute; left: 44px; top: 48px; color: var(--navy); font-family: "Montserrat", sans-serif; }
  .person__name { font-weight: 700; font-size: 36px; line-height: 40px; letter-spacing: 0.5px; }
  .person__role { font-weight: 600; font-size: 18px; margin-top: 3px; letter-spacing: 0.3px; }

  .accent-bar { position: absolute; left: 0; top: 157px; width: 14px; height: 170px; background: var(--green); }

  .contacts { position: absolute; left: 44px; top: 192px; list-style: none; }
  .contacts li { display: flex; align-items: center; height: 39px; font-size: 21px; color: var(--ink); }
  .contacts svg { width: 26px; height: 26px; margin-right: 11px; flex: none; }

  .card--back .brand { left: 460px; top: 245px; }
  .card--back .brand__dot { width: 34px; height: 34px; margin-right: 16px; }
  .card--back .brand__name { font-size: 30px; }

  .back-band { position: absolute; left: 0; bottom: 0; width: 835px; height: 130px; }
  .card--back .footer-url { top: 417px; }
  .card--back .social { top: 414px; }
</style>
</head>
<body>
  <section class="card card--front">
    <div class="brand">
      <span class="brand__dot"></span>
      <span class="brand__name">MARLO VITALITY</span>
    </div>
    <div class="footer-band">
      <span class="footer-url">WWW.MARLOVITALITY.EXAMPLE</span>
      <div class="social"><span class="social__item"></span><span class="social__item"></span></div>
    </div>
  </section>

  <section class="card card--back">
    <div class="person">
      <h1 class="person__name">TOMÁS ARRIBAL</h1>
      <p class="person__role">WELLNESS COACH, CONSULTANT &amp; TRAINER.</p>
    </div>
    <div class="accent-bar"></div>
    <ul class="contacts">
      <li>
        <svg viewBox="0 0 24 24" aria-hidden="true"><path fill="var(--navy)" d="M6.6 10.8a15.1 15.1 0 0 0 6.6 6.6l2.2-2.2a1 1 0 0 1 1-.25 11.4 11.4 0 0 0 3.6.57 1 1 0 0 1 1 1V20a1 1 0 0 1-1 1A17 17 0 0 1 3 4a1 1 0 0 1 1-1h3.5a1 1 0 0 1 1 1c0 1.25.2 2.45.57 3.57a1 1 0 0 1-.25 1z"/><path fill="none" stroke="var(--navy)" stroke-width="1.6" d="M14 2.5a8 8 0 0 1 7.5 7.5M14 6a4.5 4.5 0 0 1 4 4"/></svg>
        +34 612 480 397 (SPAIN)
      </li>
      <li>
        <svg viewBox="0 0 24 24" aria-hidden="true"><path fill="var(--navy)" d="M6.6 10.8a15.1 15.1 0 0 0 6.6 6.6l2.2-2.2a1 1 0 0 1 1-.25 11.4 11.4 0 0 0 3.6.57 1 1 0 0 1 1 1V20a1 1 0 0 1-1 1A17 17 0 0 1 3 4a1 1 0 0 1 1-1h3.5a1 1 0 0 1 1 1c0 1.25.2 2.45.57 3.57a1 1 0 0 1-.25 1z"/><path fill="none" stroke="var(--navy)" stroke-width="1.6" d="M14 2.5a8 8 0 0 1 7.5 7.5M14 6a4.5 4.5 0 0 1 4 4"/></svg>
        +1 555 318 2046 (USA)
      </li>
      <li>
        <svg viewBox="0 0 24 24" aria-hidden="true"><circle cx="12" cy="12" r="11" fill="var(--navy)"/><g fill="none" stroke="var(--white)" stroke-width="1.2"><ellipse cx="12" cy="12" rx="4.5" ry="11"/><path d="M1 12h22M3 6.5h18M3 17.5h18M12 1v22"/></g></svg>
        WWW.MARLOVITALITY.EXAMPLE
      </li>
    </ul>
    <div class="brand">
      <span class="brand__dot"></span>
      <span class="brand__name">MARLO VITALITY</span>
    </div>
    <svg class="back-band" viewBox="0 0 835 130" aria-hidden="true"><polygon points="0,49 835,0 835,130 0,130" fill="var(--navy)"/></svg>
    <span class="footer-url">WWW.MARLOVITALITY.EXAMPLE</span>
    <div class="social"><span class="social__item"></span><span class="social__item"></span></div>
  </section>
</body>
</html>
```